New Business Card Design Project

I would like my card design to look exactly like the logo, design, layout, and print of the current attached file. The only change I would like made would be for the print to say THE KMW GROUP instead of THE HALLORAN GROUP. Basically, just replace his group name with my group name. I would also like the backgroud to be the same texture and color as the attached file. I love the dark blue lettering and house logo on the card.

I am completely open to the rest of the card design. I just want something clean and simple. Only basic contact info required on the card. Maybe just name: Kyle M Warrick and cell # 555.914.2087 and email kyle@orchidhomesagent.com

```html
<!DOCTYPE html>
<html lang="en">
<head>
<meta charset="utf-8">
<title>The KMW Group – Business Card</title>
<link href="https://fonts.googleapis.com/css2?family=Open+Sans:wght@400&display=swap" rel="stylesheet">
<style>
  :root {
    --page-bg: #ffffff;
    --card-bg: #f1f0ed;
    --ink: #0f0f26;
    --accent-shadow: #9a9aa3;
  }
  html, body {
    margin: 0;
    padding: 0;
    width: 1200px;
    height: 1000px;
    overflow: hidden;
    background: var(--page-bg);
  }
  .card {
    position: absolute;
    left: 173px;
    top: 245px;
    width: 855px;
    height: 511px;
    background: var(--card-bg);
  }
  .card-shapes {
    position: absolute;
    left: 0;
    top: 0;
  }
  .brand {
    position: absolute;
    left: 280px;
    top: 186px;
    display: flex;
    align-items: center;
    gap: 24px;
  }
  .brand-square {
    width: 108px;
    height: 108px;
    background: var(--ink);
  }
  .brand-rule {
    width: 3px;
    height: 140px;
    background: var(--ink);
  }
  .brand-name {
    margin: 0;
    font-family: "Open Sans", sans-serif;
    font-weight: 400;
    font-size: 30px;
    line-height: 42px;
    letter-spacing: 0.26em;
    color: var(--ink);
  }
  .brand-name span {
    display: block;
  }
</style>
</head>
<body>
  <div class="card">
    <svg class="card-shapes" width="855" height="511" viewBox="0 0 855 511" aria-hidden="true">
      <polygon class="corner-shadow" points="29,277 29,291 449,28 429,28" fill="var(--accent-shadow)"/>
      <polygon class="corner-top" points="29,28 429,28 29,277" fill="var(--ink)"/>
      <polygon class="corner-shadow" points="825,220 825,235 425,482 405,482" fill="var(--accent-shadow)"/>
      <polygon class="corner-bottom" points="825,235 825,482 425,482" fill="var(--ink)"/>
    </svg>
    <div class="brand">
      <div class="brand-square"></div>
      <div class="brand-rule"></div>
      <h1 class="brand-name"><span>THE</span><span>KMW</span><span>GROUP</span></h1>
    </div>
  </div>
</body>
</html>
```